TEK Logistics - Banner 2.5' x 8' for 20+ locations

Need a banner designed that will pop. This banner will be displayed at over 20 of our transportation facilities. Goal is for the banner to grab the attention of employees, contractors and clients and help reinforce our mission and core values. Designed needs to include TEK Logo, our core values and mission statement. Red and Black are the main company colors and we need to stay within that theme and color pallet. Attached is a previous version that was too basic and boring. Willing to consider a design that excludes the mission statement.

Gathering more feedback

```html
<!DOCTYPE html>
<html lang="en">
<head>
<meta charset="utf-8">
<title>TEK Logistics – Core Values Banner</title>
<link href="https://fonts.googleapis.com/css2?family=Barlow+Condensed:wght@600;700&display=swap" rel="stylesheet">
<style>
  :root {
    --page-bg: #e4e4e4;
    --brand-red: #c2312f;
    --brand-red-deep: #b0272a;
    --brand-red-light: #cc403c;
    --ink: #1f1b1c;
    --white: #ffffff;
    --band-grey: #565656;
    --panel-black: #1f1f1f;
    --photo-light: #c9c9c9;
    --photo-dark: #4a4a4a;
  }
  html, body {
    margin: 0;
    padding: 0;
    width: 1200px;
    height: 938px;
    overflow: hidden;
    background: var(--page-bg);
    font-family: "Barlow Condensed", "Arial Narrow", sans-serif;
  }
  .banner {
    position: absolute;
    left: 20px;
    top: 275px;
    width: 1160px;
    height: 387px;
    overflow: hidden;
    background: linear-gradient(160deg, var(--brand-red-light) 0%, var(--brand-red) 45%, var(--brand-red-deep) 100%);
  }
  .banner-shapes {
    position: absolute;
    inset: 0;
  }
  .core-values {
    position: absolute;
    left: 24px;
    top: 26px;
    margin: 0;
    padding: 0;
    list-style: none;
  }
  .core-values li {
    position: relative;
    padding-left: 22px;
    font-size: 29px;
    line-height: 29.4px;
    font-weight: 600;
    color: var(--ink);
    text-transform: uppercase;
    letter-spacing: -0.2px;
    white-space: nowrap;
  }
  .core-values li::before {
    content: "";
    position: absolute;
    left: 0;
    top: 8px;
    border-left: 13px solid var(--ink);
    border-top: 7px solid transparent;
    border-bottom: 7px solid transparent;
  }
  .mission {
    position: absolute;
    left: 24px;
    top: 233px;
    margin: 0;
    font-size: 30px;
    line-height: 36.4px;
    font-weight: 700;
    color: var(--white);
    text-transform: uppercase;
    letter-spacing: -0.3px;
    white-space: nowrap;
  }
  .brand-name {
    position: absolute;
    left: 500px;
    top: 70px;
    display: flex;
    align-items: center;
    gap: 10px;
    font-size: 44px;
    line-height: 1;
    font-weight: 700;
    color: var(--white);
    text-transform: uppercase;
    white-space: nowrap;
  }
  .brand-dot {
    width: 14px;
    height: 14px;
    border-radius: 50%;
    background: var(--white);
  }
  .truck-photo {
    position: absolute;
    left: 608px;
    top: 140px;
    width: 526px;
    height: 208px;
    border-radius: 10px 40px 6px 6px;
    background: linear-gradient(100deg, var(--photo-dark) 0%, #8a8a8a 35%, var(--photo-light) 70%, #ededed 100%);
  }
</style>
</head>
<body>
  <section class="banner" aria-label="TEK Logistics core values banner">
    <svg class="banner-shapes" width="1160" height="387" viewBox="0 0 1160 387" aria-hidden="true">
      <polygon class="accent-band" points="1012,0 1037,0 937,387 846,387" fill="var(--band-grey)"/>
      <polygon class="dark-panel" points="1037,0 1160,0 1160,387 937,387" fill="var(--panel-black)"/>
    </svg>

    <ul class="core-values">
      <li>Do the right things for the right reasons</li>
      <li>Pursue growth and development</li>
      <li>Build a positive team atmosphere</li>
      <li>Deliver wow through service</li>
      <li>Do everything safely</li>
      <li>Have fun</li>
    </ul>

    <p class="mission">Provide the best customer experience while<br>creating an environment of growth and<br>opportunity for our customers, employees,<br>and service providers.</p>

    <div class="brand-name"><span class="brand-dot"></span>TEK Logistics</div>

    <div class="truck-photo" role="img" aria-label="Black and white photo of a semi truck with a long white trailer"></div>
  </section>
</body>
</html>
```